CEO of company needs clear business card that stands out from the rest

I need a clear business card (standard credit card size) for the CEO/Founder of our company...Brightfield Counseling. We would like to see designs that use our logo colors, which are khaki, chocolate brown, and gray. The card should be an edgy design, maybe where half the card is transparent with curves on the card, or a textured card where the logo is transparent, I don't care much for white cards. The final design should communicate a funky, edgy, and modern look, as well as stand out to have the "WOW" factor. The information we need on the card would be Name, Title, Toll free number, Phone Number, address, email address, and website.

*PLEASE SEND FRONT AND BACK OF CARDS

Card is two sided front and back please give us your front and back designs

The card should be an edgy design, maybe where half the card is transparent with curves on the card, or a textured card where the logo is transparent, I don't care much for white cards. The final design should communicate a funky, edgy, and modern look, as well as stand out to have the "WOW" factor.

Please follow these guidelines for the card

SPECS (card):

2.125 (h) x 3.375 (w) card size after cut

2.375 (h) x 3.625 (w) card with bleed

300 dpi

cmyk

1/8 bleed

allow 1/8 border for live area

I will also attached the pdf for the information listed above which includes a diagram of the card

 

All the cards need to have rounded edges

I just updated a card as an example of how you can use different fonts on a single business card, look how the name is written in script, so what I am saying is make this a card you will be proud to design and put it in your portfolio 

Reason: this race is really close and I am working with 2 designers to fine tune their designs and the weekend is slowing us down

• Our Logo
MUST HAVE PARTS OF CARD THAT ARE TRANSPARENT. See ideas that are attached.
Card is two sided front and back
• The final design should communicate a funky, edgy, and modern look, as well as stand out to have the "WOW" factor. The information we need on the card would be Name, Title, Toll free number, Phone Number, address, email address, and website.

```html
<!DOCTYPE html>
<html lang="en">
<head>
<meta charset="utf-8">
<title>Brightfield Counseling – Business Card, Front and Back</title>
<link rel="stylesheet" href="https://fonts.googleapis.com/css2?family=Tinos&family=Arimo:wght@700&family=Lato:wght@400&display=swap">
<style>
  :root {
    --page: #ece9e5;
    --card-gray: #7a7a7a;
    --frost-light: #f1f1f1;
    --frost-mid: #dcdcdc;
    --brand-brown: #8a4a1e;
    --name-ink: #f2f2f2;
    --title-ink: #111111;
    --contact-ink: #ffffff;
  }
  * { margin: 0; padding: 0; box-sizing: border-box; }
  html, body {
    width: 1200px; height: 900px; overflow: hidden;
    background: var(--page);
  }
  .card-set {
    position: absolute; left: 60px; top: 286px;
    display: flex; gap: 40px;
  }
  .card {
    position: relative; width: 520px; height: 328px;
    background: var(--card-gray); overflow: hidden;
    box-shadow: 0 6px 14px rgba(0,0,0,0.22);
  }
  .card--front { border-radius: 12px 46px 46px 12px; }
  .card--back { border-radius: 46px 12px 12px 46px; }
  .frost-panel { position: absolute; inset: 0; width: 520px; height: 328px; }

  .brand {
    position: absolute; left: 52px; top: 72px;
    display: flex; align-items: center; gap: 8px;
    font-family: "Tinos", serif; font-size: 24px;
    color: var(--brand-brown);
  }
  .brand-dot {
    width: 14px; height: 14px; border-radius: 50%;
    background: var(--brand-brown);
  }
  .holder {
    position: absolute; left: 74px; top: 228px; width: 220px; text-align: center;
  }
  .holder-name {
    font-family: "Tinos", serif; font-size: 27px; color: var(--name-ink);
    white-space: nowrap;
  }
  .holder-title {
    margin-top: 3px;
    font-family: "Arimo", sans-serif; font-weight: 700; font-size: 12px;
    letter-spacing: 0.5px; color: var(--title-ink);
  }

  .contact {
    position: absolute; right: 34px; text-align: right; color: var(--contact-ink);
  }
  .contact--lines {
    top: 78px; font-family: "Lato", sans-serif; font-size: 17px; line-height: 27px;
  }
  .contact--address {
    top: 224px; font-family: "Tinos", serif; font-size: 15px; line-height: 21px;
  }
</style>
</head>
<body>
  <main class="card-set">
    <section class="card card--front" aria-label="Card front">
      <svg class="frost-panel" viewBox="0 0 520 328" role="img" aria-label="Frosted clear panel with embossed emblem">
        <defs>
          <linearGradient id="frost-front" x1="0" y1="0" x2="1" y2="1">
            <stop offset="0" stop-color="var(--frost-light)"/>
            <stop offset="1" stop-color="var(--frost-mid)"/>
          </linearGradient>
        </defs>
        <path d="M285,0 C250,70 300,140 345,190 C385,235 385,290 372,328 L520,328 L520,0 Z" fill="url(#frost-front)"/>
      </svg>
      <div class="brand">
        <span class="brand-dot"></span>
        <span class="brand-name">Brightfield Counseling</span>
      </div>
      <div class="holder">
        <p class="holder-name">Darren Whitfield</p>
        <p class="holder-title">FOUNDER / CEO</p>
      </div>
    </section>

    <section class="card card--back" aria-label="Card back">
      <svg class="frost-panel" viewBox="0 0 520 328" role="img" aria-label="Frosted clear panel with embossed emblem">
        <defs>
          <linearGradient id="frost-back" x1="1" y1="0" x2="0" y2="1">
            <stop offset="0" stop-color="var(--frost-light)"/>
            <stop offset="1" stop-color="var(--frost-mid)"/>
          </linearGradient>
        </defs>
        <path d="M0,0 L235,0 C270,70 230,150 190,200 C160,240 150,290 148,328 L0,328 Z" fill="url(#frost-back)"/>
      </svg>
      <div class="contact contact--lines">
        <p>f. 555.214.7260</p>
        <p>t. 555.301.4440</p>
        <p>Toll free: 1.800.555.0182</p>
        <p>www.brightfieldcounseling.com</p>
      </div>
      <div class="contact contact--address">
        <p>418 Maple Crest Dr. N.W. Suite 210</p>
        <p>Marietta GA 30060</p>
        <p>dwhitfield@brightfieldcounseling.com</p>
      </div>
    </section>
  </main>
</body>
</html>
```